Wine Shop Banners

Banner graphic/images required
Require banner images to match the present online wine shop.

www.kelterhaus-traube.de

The wine-shop presently has a very clean, simple design, lots of white space, which is very much the trend at the moment.

Requirements
Images or graphic design for present banners visible on the homepage

The colour and feeling of the banners must fit in with the present clean, simple design.

Work required
3 large slide-card/banners (can be more) and 3 smaller fixed banners below. Please view website to see present position of banners.

LARGE BANNERS x 3

Something special with white background within the banner space
White background on each slide-card. Small individual graphic image in the middle of the slide card. This could be either a simple element of wine:
ingredients, fruit (grape), bottle, cork, old bottle label etc. just displaying one item on each slide-card. Preferably with high quality graphic features.

Note:
We are trying the steer away from the classic stereotype wineshop design. The image/s should have a higher, individual graphic touch, which gives the design something different. Sometimes such artistic work is displayed in steampunk or even in nostalgic design, which leaves the viewer slightly memorized with the content.
To clarify: we are not looking for a full steampunk design but possibly certain elements of this will give you an idea what we mean. That is to say, the design can go slightly in this direction without going over the top. Something small but very eye-catching.

SMALLER BANNERS x 3

One idea is:
Showing a symbol e.g. - discount sign "%" against a white background but again with a high graphic quality.

Target Market(s)

People interested in purchasing wine.
Ages approx. 25 to 65

Industry/Entity Type

Shop

Requirements
Must have
• Something special with white background
• Small individual graphic image in the middle of the slide card.
Nice to have
• The image/s should have a higher, individual graphic touch, which gives the design something different. Something that leaves the viewer slightly memorized with the content.
Should not have
• Not the typical classical design that is often seen on wine shops.

```html
<!DOCTYPE html>
<html lang="en">
<head>
<meta charset="utf-8">
<title>Celebrate Your Anniversary With Taste</title>
<link rel="stylesheet" href="https://fonts.googleapis.com/css2?family=Tinos&display=swap">
<style>
  :root {
    --canvas: #ffffff;
    --panel-edge: #ececec;
    --panel-center: #ffffff;
    --headline: #a3282c;
    --headline-dark: #7e1a1e;
    --headline-light: #c0474a;
    --wine-pale: #f4eec4;
    --wine-gold: #ddcf86;
    --glass: #f3f3f3;
  }
  html, body {
    margin: 0;
    padding: 0;
    width: 1200px;
    height: 900px;
    overflow: hidden;
    background: var(--canvas);
  }
  .canvas {
    position: relative;
    width: 1200px;
    height: 900px;
    background: var(--canvas);
  }
  .banner {
    position: absolute;
    left: 66px;
    top: 137px;
    width: 1064px;
    height: 491px;
    background: var(--panel-center);
    box-shadow: inset 0 0 40px 14px var(--panel-edge);
    overflow: hidden;
  }
  .banner__art {
    position: absolute;
    left: 52px;
    top: 68px;
    width: 284px;
    height: 365px;
    display: block;
  }
  .banner__headline {
    position: absolute;
    left: 322px;
    top: 74px;
    width: 700px;
    margin: 0;
    font-family: "Tinos", "Times New Roman", serif;
    font-weight: 400;
    font-size: 96px;
    line-height: 116px;
    letter-spacing: 0;
    text-align: center;
    white-space: nowrap;
    color: var(--headline);
    transform: scaleX(0.8);
    transform-origin: 50% 0;
    text-shadow:
      1px 1px 0 var(--headline-dark),
      -1px -1px 0 var(--headline-light),
      2px 3px 3px rgba(0, 0, 0, 0.18);
  }
  .banner__headline span { display: block; }
</style>
</head>
<body>
  <main class="canvas">
    <section class="banner">
      <svg class="banner__art" viewBox="0 0 284 365" role="img" aria-label="Illustration of two glasses of white wine clinking in a toast">
        <defs>
          <linearGradient id="wine-tone" x1="0" y1="0" x2="0" y2="1">
            <stop offset="0" stop-color="#f3f3f3"/>
            <stop offset="0.25" stop-color="#f4eec4"/>
            <stop offset="0.45" stop-color="#ddcf86"/>
            <stop offset="0.6" stop-color="#f3f3f3"/>
            <stop offset="1" stop-color="#ffffff"/>
          </linearGradient>
        </defs>
        <rect x="0" y="0" width="284" height="365" rx="20" fill="url(#wine-tone)"/>
      </svg>
      <h1 class="banner__headline">
        <span>CELEBRATE YOUR</span>
        <span>ANNIVERSARY</span>
        <span>WITH TASTE</span>
      </h1>
    </section>
  </main>
</body>
</html>
```